Personal Chef Business Card Design

My company, Simmerly, is a personal in-home chef service that caters to clients' needs, but I am not a caterer. The types of services that I provide range from : weekly menus for busy families, special menus for specific diets, custom menus, private parties, intimate dinners, and brunch parties. My cooking style is seasonal and simple with the option of a variety of cuisines. I like colorful and simple business cards. My business is just getting started as I will be the only employee for now. I would like to be able to use the design on the card for my logo also. I don't know if logo design is a different service altogether.

If you can convince me to go with double-sided, then so be it, but until then, I'll stick with singe-sided.

Target Market(s)

busy families, health conscious, private parties, brunch parties, dinner parties

Industry/Entity Type

Chef

Contact Information for Business Card

Ross Tamblyn
rosstamblyn@mailvora.com
434-817-2290
Simmerly Personal Chef Service
Serving the DC/VA/MD area

Font styles to use
Serif
Sans Serif
Decorative
Script
Other font styles liked:
• Anything

Requirements
Must have
• I will be using the illustration as my logo so that I can use it for promotional merchandise.

```html
<!DOCTYPE html>
<html lang="en">
<head>
<meta charset="utf-8">
<title>Simmerly Personal Chef Service – Business Card</title>
<link rel="stylesheet" href="https://fonts.googleapis.com/css2?family=Montserrat:wght@700;800&family=Hind:wght@400;600&display=swap">
<style>
  :root {
    --backdrop: #3d2b25;
    --card: #fbfbfb;
    --brand-blue: #3f6fae;
    --rule-blue: #4a78b4;
    --ink: #3a3a3a;
    --ink-soft: #505257;
    --panel-top: #f1f3f6;
    --panel-bottom: #e3e8ee;
  }
  * { margin: 0; padding: 0; box-sizing: border-box; }
  html, body {
    width: 1200px;
    height: 1000px;
    overflow: hidden;
    background: var(--backdrop);
  }
  .business-card {
    position: absolute;
    left: 260px;
    top: 310px;
    width: 680px;
    height: 380px;
    background: var(--card);
    box-shadow: 0 6px 18px rgba(0,0,0,0.35);
    overflow: hidden;
  }
  .brand-name {
    position: absolute;
    left: 0;
    right: 0;
    top: 66px;
    text-align: center;
    font-family: "Montserrat", sans-serif;
    font-weight: 800;
    font-size: 94px;
    letter-spacing: 2px;
    line-height: 1;
    color: var(--brand-blue);
  }
  .tagline-rule {
    position: absolute;
    left: 78px;
    width: 530px;
    height: 2px;
  }
  .tagline-rule--top { top: 192px; }
  .tagline-rule--bottom { top: 244px; }
  .tagline {
    position: absolute;
    left: 76px;
    width: 536px;
    top: 204px;
    font-family: "Hind", sans-serif;
    font-weight: 400;
    font-size: 23.5px;
    letter-spacing: 0.3px;
    line-height: 1.3;
    color: var(--ink);
    white-space: nowrap;
  }
  .contact-panel {
    position: absolute;
    left: 78px;
    width: 530px;
    top: 247px;
    bottom: 0;
    background: linear-gradient(180deg, var(--panel-top), var(--panel-bottom));
    text-align: center;
    font-family: "Hind", sans-serif;
    font-weight: 600;
    color: var(--ink-soft);
  }
  .contact-name {
    margin-top: 22px;
    font-size: 25px;
    letter-spacing: 1px;
    line-height: 1.2;
  }
  .contact-email {
    margin-top: 4px;
    font-size: 21px;
    line-height: 1.25;
  }
  .contact-phone {
    margin-top: 4px;
    font-size: 22px;
    letter-spacing: 1px;
    line-height: 1.25;
  }
</style>
</head>
<body>
  <div class="business-card">
    <div class="brand-name">SIMMERLY</div>

    <svg class="tagline-rule tagline-rule--top" viewBox="0 0 530 2" preserveAspectRatio="none" aria-hidden="true">
      <line x1="0" y1="1" x2="530" y2="1" stroke="var(--rule-blue)" stroke-width="2" stroke-linecap="round"/>
    </svg>
    <p class="tagline">Personal Chef Service Serving the DC/VA/MD Area</p>
    <svg class="tagline-rule tagline-rule--bottom" viewBox="0 0 530 2" preserveAspectRatio="none" aria-hidden="true">
      <line x1="0" y1="1" x2="530" y2="1" stroke="var(--rule-blue)" stroke-width="2" stroke-linecap="round"/>
    </svg>

    <div class="contact-panel">
      <p class="contact-name">DARA WHITCOMBE</p>
      <p class="contact-email">darawhitcombe@mailvora.com</p>
      <p class="contact-phone">434-817-2290</p>
    </div>
  </div>
</body>
</html>
```